Healthcare Recruitment Agency Brochure

We need our current Brochure updated as its old and dated. The brochure will be for our current and potential Clients and should provide all the necessary information regarding our services, but in a well presented, easy reading format which echoes our company Brand. The company supplies Healthcare establishments with trained healthcare Staff which can be in a variety of settings.
UPDATE: Following the submission of many designs we would like to amend the information/content to be included in the brochure and have uploaded additional information. We would like an 8 page booklet with the various sections spread out so as not to look to 'wordy' page 1 Front cover, 2 About Us, 3 Our Service, 4 Our promise, 5 Our Staff, 6 Our Ethos, 7 What Our Clients Say/Testimonials, 8 Contact Us/Back page. Please if using pictures (which is welcomed) steer away from the surgical/doctor type. We mainly provide care to the Elderly within Nursing and Residential Homes and Support Environments. Thanks
Updates

Target Market(s)

Healthcare clientell

Industry/Entity Type

Healthcare

Requirements
Must have
• Pictures, animation, easy reading, informative, tie in with website theme www.carewellstaffline.example
Nice to have
• open to ideas
Should not have
• very long text paragraphs

```html
<!DOCTYPE html>
<html lang="en">
<head>
<meta charset="utf-8">
<title>Carewell Staffline – Client Brochure Pages</title>
<link rel="stylesheet" href="https://fonts.googleapis.com/css2?family=Source+Sans+3:wght@400;600;700&display=swap">
<style>
:root{
  --blue:#1b55a8;
  --teal:#17a58a;
  --text:#555a5f;
  --paper:#ffffff;
  --ground:#dedede;
}
*{box-sizing:border-box;margin:0;padding:0}
html,body{width:1200px;height:606px;overflow:hidden}
body{background:var(--ground);font-family:"Source Sans 3",sans-serif;position:relative;color:var(--text)}
.page{position:absolute;top:76px;width:324px;height:459px;background:var(--paper);overflow:hidden;box-shadow:0 2px 6px rgba(0,0,0,.25)}
.page--about{left:97px}
.page--staff{left:446px}
.page--ethos{left:797px}
.abs{position:absolute}
.brand{left:12px;top:20px;display:flex;align-items:center;gap:4px;font-size:11px;font-weight:600;color:var(--blue);line-height:1}
.brand__dot{width:7px;height:7px;border-radius:50%;background:var(--teal)}
.tab{height:10px;font-size:7.5px;font-weight:700;line-height:10px;padding-left:15px}
.tab--outline{left:0;top:57px;width:66px;color:var(--blue);border:1px solid var(--teal);border-left:none;border-radius:0 6px 6px 0}
.tab--filled{left:0;top:59px;width:64px;background:var(--teal);color:#fff;border-radius:0 6px 6px 0;padding-left:15px}
.copy{font-size:5.4px;line-height:7px;color:var(--blue)}
.photo-round{left:176px;top:0;width:164px;height:164px;border-radius:50%;border:5px solid var(--teal);background:radial-gradient(circle at 55% 45%,#e7d7c9,#9fcfca 55%,#5fb3ab);z-index:2}
.band-blue{left:8px;top:150px;width:316px;height:36px;background:var(--blue);z-index:1}
.band-blue p{position:absolute;left:6px;bottom:6px;font-size:5px;color:#fff;white-space:nowrap}
.rule{height:1.5px;background:var(--teal)}
.services{left:15px;top:206px;width:300px;list-style:none}
.services li{display:flex;align-items:center;gap:9px;font-size:5.5px;line-height:7px;height:23.5px}
.icon{flex:none;width:16px;height:16px;border-radius:50%;background:var(--teal);display:flex;align-items:center;justify-content:center}
.footer{left:0;top:439px;width:324px;height:20px}
.footer__teal{left:0;top:0;width:20px;height:20px;background:var(--teal);clip-path:polygon(0 0,100% 0,60% 100%,0 100%)}
.footer__badge{left:26px;top:3px;width:14px;height:10px;background:var(--blue);opacity:.85}
.footer__badge-text{left:25px;top:13px;font-size:3.8px;color:var(--blue)}
.footer__band{left:56px;top:0;width:268px;height:20px;background:var(--blue);clip-path:polygon(8px 0,100% 0,100% 100%,0 100%);color:#fff;font-size:4.3px;line-height:20px;padding-left:11px;white-space:nowrap}
.photo-wide{left:0;top:64px;width:324px;height:121px;background:linear-gradient(100deg,#cfe1c3 0%,#8fb27d 30%,#d9694b 55%,#6f8f56 80%,#a9c496 100%)}
.lead{left:20px;top:195px;width:284px;text-align:center;font-size:7px;line-height:9px;color:var(--blue)}
.checks{left:17px;width:289px;display:grid;grid-template-columns:repeat(5,55px);gap:3.5px}
.checks--one{top:232px}
.checks--two{top:312px}
.check{position:relative;height:61px;border:0.8px solid var(--teal);border-radius:4px;text-align:center;font-size:5.2px;line-height:6.6px;color:var(--text);padding:19px 3px 0}
.check--dense{font-size:4.4px;line-height:5.3px;padding-top:15px}
.check .icon{position:absolute;left:19px;top:-7px;width:17px;height:17px;background:var(--blue);border:1.5px solid #fff}
.note{left:15px;width:294px;text-align:center;font-size:5.4px;line-height:8px}
.ethos-title{right:12px;top:28px;text-align:right;font-weight:700;font-size:8px;line-height:10px}
.ethos-title span{display:block}
.ethos-title .t1{color:var(--blue)}
.ethos-title .t2{color:var(--teal)}
.photo-soft{left:0;top:57px;width:324px;height:123px;background:linear-gradient(90deg,#ffffff 0%,#eef3f2 25%,#d8e6e2 50%,#c9b7a9 75%,#9fd3c7 100%)}
.value{left:36px;width:280px}
.value h3{font-size:8.5px;font-weight:700;color:var(--teal);font-variant:small-caps;letter-spacing:.1px}
.value h3::first-letter{color:var(--blue);font-size:11px}
.value p{font-size:5.6px;line-height:8px;margin-top:4px}
.mark{left:12px;width:14px;height:14px;border-radius:50%;border:1.3px solid var(--blue)}
</style>
</head>
<body>

<!-- About Us -->
<section class="page page--about">
  <div class="abs brand"><span class="brand__dot"></span>Carewell Staffline</div>
  <div class="abs photo-round" role="img" aria-label="Smiling carer in teal uniform with an elderly gentleman"></div>
  <div class="abs tab tab--outline">ABOUT US</div>
  <p class="abs copy" style="left:15px;top:71px;width:162px">With over 15 years of experience Carewell Staffline specialises in reliable recruitment solutions for the healthcare sector. We are TSA accredited so you can rest assured that we will always be working in line with current legislation and guidelines.</p>
  <p class="abs copy" style="left:15px;top:107px;width:162px">We strive for excellence in every aspect of our service, this includes ensuring that we are always fair, honest, and supportive of our temporary staff members, which is why we are a National Living Wage Employer.</p>
  <div class="abs rule" style="left:8px;top:147px;width:145px"></div>
  <div class="abs band-blue"><p>We know that our Clients often have a lot on their plate, which is why we pride ourselves on being extremely accommodating:</p></div>
  <div class="abs rule" style="left:8px;top:188px;width:308px"></div>
  <ul class="abs services">
    <li><span class="icon"><svg width="9" height="9" viewBox="0 0 10 10"><circle cx="5" cy="5" r="4" fill="none" stroke="#fff"/><path d="M5 2.5V5h2" stroke="#fff" fill="none"/></svg></span>We can visit you at a time to suit you, to discuss your requirements and our service.</li>
    <li><span class="icon"><svg width="9" height="9" viewBox="0 0 10 10"><rect x="2" y="1" width="6" height="8" fill="none" stroke="#fff"/><path d="M3.5 4h3M3.5 6h3" stroke="#fff"/></svg></span>We will give you our client application pack including everything you need to know, to start booking staff from Carewell Staffline we simply need a completed client account form.</li>
    <li><span class="icon"><svg width="9" height="9" viewBox="0 0 10 10"><path d="M2 1v4a3 3 0 0 0 6 0V1" fill="none" stroke="#fff"/></svg></span>We have staff available to work at the drop of a hat-we understand the need for urgency and will make it our mission to try to help you every time.</li>
    <li><span class="icon"><svg width="9" height="9" viewBox="0 0 10 10"><path d="M2 1.5l2 0 1 2-1.2 1a5 5 0 0 0 2.2 2.2l1-1.2 2 1v2c-4 .5-7.5-3-7-7z" fill="#fff"/></svg></span>Our friendly office staff will always be at the end of the phone to deal with your requests;<br>we never outsource to call centres.</li>
    <li><span class="icon"><svg width="9" height="9" viewBox="0 0 10 10"><circle cx="4" cy="3" r="2" fill="#fff"/><path d="M1 9a3 3 0 0 1 6 0z" fill="#fff"/></svg></span>We will never leave you waiting and always be honest and realistic in telling you whether we can help.</li>
    <li style="height:27px"><span class="icon"><svg width="9" height="9" viewBox="0 0 10 10"><path d="M2 5l2 2 4-4" stroke="#fff" stroke-width="1.4" fill="none"/></svg></span>When you have booked a staff member you will always receive their compliance form, in a format that suits you.</li>
    <li style="height:24px"><span class="icon"><svg width="9" height="9" viewBox="0 0 10 10"><circle cx="3" cy="4" r="1.5" fill="#fff"/><circle cx="7" cy="4" r="1.5" fill="#fff"/><path d="M0.5 9a2.5 2.5 0 0 1 5 0zM4.5 9a2.5 2.5 0 0 1 5 0z" fill="#fff"/></svg></span>You can choose how frequently and in which format we send you your staff rotas, we will be completely flexible to your needs.</li>
    <li><span class="icon"><svg width="9" height="9" viewBox="0 0 10 10"><path d="M1 2h8v5H4l-2 2V7H1z" fill="#fff"/></svg></span>We are always interested in how we could improve; we will regularly review our service and come and visit you when requested.</li>
    <li><span class="icon"><svg width="9" height="9" viewBox="0 0 10 10"><rect x="2" y="1" width="6" height="8" fill="#fff"/><path d="M3.5 4h3M3.5 6h3" stroke="#17a58a"/></svg></span>We will regularly send you monitoring forms so you can quickly and easily pass on your feedback about the staff members we are sending you.</li>
  </ul>
  <div class="abs footer">
    <div class="abs footer__teal"></div>
    <div class="abs footer__badge"></div>
    <div class="abs footer__badge-text">Member</div>
    <div class="abs footer__band">Registered in England No. 10987654 Carewell Staffline Services Ltd, 14 Orchard Row, Ashford, Kent, TN23 4QX</div>
  </div>
</section>

<!-- Our Staff -->
<section class="page page--staff">
  <div class="abs brand"><span class="brand__dot"></span>Carewell Staffline</div>
  <div class="abs photo-wide" role="img" aria-label="Carer pushing a smiling elderly lady in a wheelchair along a garden path"></div>
  <div class="abs tab tab--filled">OUR STAFF</div>
  <div class="abs rule" style="left:15px;top:188px;width:296px"></div>
  <p class="abs lead">All our candidates go through a thorough vetting and recruitment process and only ever commence assignments after the following :</p>
  <div class="abs checks checks--one">
    <div class="check"><span class="icon"></span>A face-to-face interview and skills assessment has been undertaken</div>
    <div class="check"><span class="icon"></span>Full employment history has been submitted</div>
    <div class="check"><span class="icon"></span>Right to work has been recorded and verified</div>
    <div class="check"><span class="icon"></span>Fitness to work has been declared</div>
    <div class="check"><span class="icon"></span>Two work related references have been obtained and verified</div>
  </div>
  <div class="abs checks checks--two">
    <div class="check"><span class="icon"></span>An enhanced DBS Certificate has been provided</div>
    <div class="check check--dense"><span class="icon"></span>In date, sufficient training certificates have been provided and verified or in house training courses have been attended and certificates have been issued.</div>
    <div class="check"><span class="icon"></span>Registration with the appropriate bodies has been verified for Registered Nurses.</div>
    <div class="check"><span class="icon"></span>A shadow shift has been completed if it is a brand new staff member</div>
    <div class="check"><span class="icon"></span>An ID Badge, uniform, and timesheets have been issued</div>
  </div>
  <p class="abs note" style="top:384px">We understand that it is imperative for our clients to only have extremely competent, fully trained staff supporting their existing team. We are proud to cover the standards set with-in the Care Certificate in the training modules that we deliver to our staff.</p>
  <p class="abs note" style="top:416px">All training is refreshed on an annual basis and we ensure that up to date certificates are held by all staff at all times.</p>
  <div class="abs footer">
    <div class="abs footer__teal"></div>
    <div class="abs footer__badge"></div>
    <div class="abs footer__badge-text">Member</div>
    <div class="abs footer__band">Registered in England No. 10987654 Carewell Staffline Services Ltd, 14 Orchard Row, Ashford, Kent, TN23 4QX</div>
  </div>
</section>

<!-- Our Ethos -->
<section class="page page--ethos">
  <div class="abs brand"><span class="brand__dot"></span>Carewell Staffline</div>
  <div class="abs ethos-title"><span class="t1">OUR ETHOS</span><span class="t2">CAREWELL STAFFLINE SERVICES LTD</span></div>
  <div class="abs photo-soft" role="img" aria-label="Carer greeting a smiling elderly lady beside a window with pink flowers"></div>
  <div class="abs rule" style="left:8px;top:185px;width:308px"></div>
  <span class="abs mark" style="top:221px"></span>
  <div class="abs value" style="top:218px"><h3>Honesty and Integrity.</h3><p>We pride ourselves on being direct and straightforward in all our communi-cation with our clients and potential candidates.</p></div>
  <span class="abs mark" style="top:279px"></span>
  <div class="abs value" style="top:276px"><h3>Dedication.</h3><p>Our consultants aim to fully understand the requirements of our clients and candidates in order to find mutually beneficial solutions.</p></div>
  <span class="abs mark" style="top:337px"></span>
  <div class="abs value" style="top:334px"><h3>Service Excellence.</h3><p>We aim to always deliver superior services to help both employers and can-didates achieve their goals.</p></div>
  <span class="abs mark" style="top:391px"></span>
  <div class="abs value" style="top:388px"><h3>Leadership.</h3><p>Our purpose is to become leaders in the healthcare recruitment sector, raising the bar for the entire industry.</p></div>
  <div class="abs footer">
    <div class="abs footer__teal"></div>
    <div class="abs footer__badge"></div>
    <div class="abs footer__badge-text">Member</div>
    <div class="abs footer__band">Registered in England No. 10987654 Carewell Staffline Services Ltd, 14 Orchard Row, Ashford, Kent, TN23 4QX</div>
  </div>
</section>

</body>
</html>
```